Fireworks company

COLORFUL design, incorporating logo (attached).
Information to be included:
PO BOX 4829
Marlow Vale 3891
Ph 03 5461 8237
Fax 03 5387 9216
Email sales@brindarockets.com.au
Web www.brindarockets.com.au

Check out our website for more inspiration? :-)

```html
<!DOCTYPE html>
<html lang="en">
<head>
<meta charset="utf-8">
<title>Brinda Rockets Letterhead</title>
<link href="https://fonts.googleapis.com/css2?family=Open+Sans:wght@400;600;800&display=swap" rel="stylesheet">
<style>
  :root {
    --backdrop: #8a8a8a;
    --paper: #ffffff;
    --band: #050505;
    --accent: #f0901e;
    --text-light: #f2f2f2;
    --watermark: #fbe3d6;
    --spark-warm: #e08a2a;
    --spark-cool: #5a8fb8;
  }
  * { box-sizing: border-box; margin: 0; padding: 0; }
  html, body {
    width: 1200px; height: 1000px; overflow: hidden;
    background: var(--backdrop);
    font-family: "Open Sans", Arial, sans-serif;
  }
  .letterhead {
    position: absolute; left: 252px; top: 50px;
    width: 696px; height: 900px;
    background: var(--paper);
    box-shadow: 0 4px 14px rgba(0,0,0,0.35);
    overflow: hidden;
  }
  .header-band {
    position: absolute; left: 0; top: 0; width: 100%; height: 106px;
    background: var(--band);
    border-bottom: 3px solid var(--accent);
  }
  .burst {
    position: absolute;
    background: radial-gradient(circle at 50% 50%, #ffd45a 0%, var(--spark-warm) 30%, #6a3a10 55%, var(--band) 75%);
  }
  .burst-left { left: 0; top: 0; width: 72px; height: 56px; }
  .burst-right {
    right: 0; top: 0; width: 156px; height: 92px;
    background:
      radial-gradient(circle at 22% 45%, #d8d040 0%, #7a7a20 25%, transparent 45%),
      radial-gradient(circle at 55% 55%, #ffb048 0%, var(--spark-warm) 22%, transparent 48%),
      radial-gradient(circle at 86% 22%, #cfe8ff 0%, var(--spark-cool) 18%, transparent 38%),
      var(--band);
  }
  .brand {
    position: absolute; left: 66px; top: 26px;
    display: flex; align-items: center; gap: 10px;
  }
  .brand-name {
    color: var(--text-light); font-weight: 800;
    font-size: 25px; line-height: 26px; letter-spacing: 1px;
  }
  .brand-dot { width: 12px; height: 12px; border-radius: 50%; background: var(--accent); }
  .contact-list {
    position: absolute; left: 318px; top: 24px; z-index: 2;
    list-style: none; color: var(--text-light);
    font-size: 9px; line-height: 15px; white-space: nowrap;
  }
  .contact-list li { display: flex; align-items: center; gap: 7px; }
  .contact-list li:nth-child(2) { padding-left: 8px; }
  .contact-list li:nth-child(3) { padding-left: 16px; }
  .contact-list li:nth-child(4) { padding-left: 24px; }
  .contact-list li:nth-child(5) { padding-left: 36px; }
  .icon { width: 9px; height: 9px; flex: none; }
  .watermark {
    position: absolute; left: 168px; top: 480px; width: 380px;
    display: flex; align-items: center; gap: 14px;
  }
  .watermark-name {
    color: var(--watermark); font-weight: 800;
    font-size: 46px; line-height: 48px; letter-spacing: 2px;
  }
  .watermark-dot { width: 26px; height: 26px; border-radius: 50%; background: var(--watermark); }
  .footer-band {
    position: absolute; left: 0; bottom: 0; width: 100%; height: 12px;
    background: var(--band);
  }
  .footer-spark {
    position: absolute; left: 344px; bottom: 0; width: 8px; height: 12px;
    background: linear-gradient(100deg, transparent 30%, var(--accent) 50%, transparent 70%);
  }
</style>
</head>
<body>
  <main class="letterhead">
    <header class="header-band">
      <div class="burst burst-left" role="img" aria-label="Colourful firework burst"></div>
      <div class="brand">
        <span class="brand-name">BRINDA<br>ROCKETS</span>
        <span class="brand-dot"></span>
      </div>
      <div class="burst burst-right" role="img" aria-label="Cluster of colourful firework bursts"></div>
      <ul class="contact-list">
        <li><svg class="icon" viewBox="0 0 10 10"><rect width="10" height="10" rx="2" fill="#f0901e"/><path d="M3 2.5c0 3 1.5 4.5 4.5 4.5l.5-1-1.3-.8-.6.6C5.2 5.4 4.6 4.8 4.2 3.9l.6-.6L4 2z" fill="#050505"/></svg>Ph 03 5461 8237</li>
        <li><svg class="icon" viewBox="0 0 10 10"><rect width="10" height="10" rx="2" fill="#f0901e"/><rect x="2.5" y="2" width="5" height="6" fill="#050505"/></svg>Fax 03 5387 9216</li>
        <li><svg class="icon" viewBox="0 0 10 10"><rect width="10" height="10" rx="2" fill="#f0901e"/><path d="M2 3h6v4H2zM2 3l3 2.4L8 3" fill="none" stroke="#050505" stroke-width="0.9"/></svg>sales@brindarockets.com.au</li>
        <li><svg class="icon" viewBox="0 0 10 10"><rect width="10" height="10" rx="2" fill="#f0901e"/><circle cx="5" cy="5" r="2.8" fill="none" stroke="#050505" stroke-width="0.9"/><path d="M2.2 5h5.6M5 2.2v5.6" stroke="#050505" stroke-width="0.7"/></svg>www.brindarockets.com.au</li>
        <li><svg class="icon" viewBox="0 0 10 10"><rect width="10" height="10" rx="2" fill="#f0901e"/><path d="M5 8.5 2.8 5A2.4 2.4 0 1 1 7.2 5z" fill="#050505"/></svg>PO BOX 4829, Marlow Vale 3891</li>
      </ul>
    </header>

    <div class="watermark" aria-hidden="true">
      <span class="watermark-name">BRINDA<br>ROCKETS</span>
      <span class="watermark-dot"></span>
    </div>

    <footer class="footer-band">
      <div class="footer-spark"></div>
    </footer>
  </main>
</body>
</html>
```